Business card design needed

We are a gardening company who handle:
All Forms of gardens work including
Mowing
Pruning
edging
weeding
Poisoning
Landscaping
Minor Stump Removal
Rubbish Removal
and more

I want a card that look professional not cartoon style

Harlow Yards and Lawncare Service

Dean Marsholt
0486259041

```html
<!DOCTYPE html>
<html lang="en">
<head>
<meta charset="utf-8">
<title>Harlow Yards and Lawncare Service – Business Card</title>
<link rel="stylesheet" href="https://fonts.googleapis.com/css2?family=Gabriela&display=swap">
<style>
  :root {
    --card-bg: #231f20;
    --brand-green: #3fa84a;
    --text-light: #ffffff;
    --leaf-light: #7fd05a;
    --leaf-mid: #4fb13a;
    --leaf-dark: #2f8a2a;
  }
  html, body {
    margin: 0;
    padding: 0;
    width: 1200px;
    height: 693px;
    overflow: hidden;
    background: var(--card-bg);
  }
  .card {
    position: relative;
    width: 1200px;
    height: 693px;
    background: var(--card-bg);
    overflow: hidden;
    font-family: "Gabriela", Georgia, serif;
  }
  .leaf-panel {
    position: absolute;
    left: 0;
    top: 0;
  }
  .text-column {
    position: absolute;
    left: 0;
    top: 0;
    width: 700px;
    height: 693px;
    text-align: center;
  }
  .line {
    position: absolute;
    left: 0;
    width: 700px;
    margin: 0;
    white-space: nowrap;
    line-height: 1;
  }
  .company-name {
    color: var(--brand-green);
    font-size: 56px;
    font-weight: 400;
    letter-spacing: -0.5px;
  }
  .company-name.first { top: 68px; }
  .company-name.second { top: 182px; }
  .services {
    color: var(--text-light);
    font-size: 27px;
  }
  .services.row-1 { top: 314px; }
  .services.row-2 { top: 372px; }
  .services.row-3 { top: 438px; }
  .contact-name {
    color: var(--brand-green);
    font-size: 36px;
    top: 543px;
  }
  .contact-phone {
    color: var(--brand-green);
    font-size: 34px;
    top: 605px;
  }
</style>
</head>
<body>
  <div class="card">
    <svg class="leaf-panel" width="1200" height="693" viewBox="0 0 1200 693" role="img" aria-label="Close-up photograph of a green leaf showing its vein pattern">
      <defs>
        <radialGradient id="leafGlow" cx="0.55" cy="0.45" r="0.6">
          <stop offset="0" stop-color="var(--leaf-light)"/>
          <stop offset="0.6" stop-color="var(--leaf-mid)"/>
          <stop offset="1" stop-color="var(--leaf-dark)"/>
        </radialGradient>
      </defs>
      <circle cx="1259" cy="346" r="468" fill="url(#leafGlow)"/>
    </svg>

    <div class="text-column">
      <h1 class="line company-name first">Harlow Yards</h1>
      <h1 class="line company-name second">and Lawncare Service</h1>
      <p class="line services row-1">mowing - pruning - edging</p>
      <p class="line services row-2">weeding - poisoning - landscaping</p>
      <p class="line services row-3">minor stump removal - rubbish removal</p>
      <p class="line contact-name">Dean Marsholt</p>
      <p class="line contact-phone">0486259041</p>
    </div>
  </div>
</body>
</html>
```